Norvale Email Signature Banners – Fabrication Capability Series

www.Norvale.com.au is an Australian engineering and fabrication company specialising in fabrication and welding of :
steel piping spools,
skids and frames,
small volume process steel tanks
and general steel fabrication
We require four distinct banner designs for use in Teldrin Quillmark email signatures. Each banner will highlight a specific capability while maintaining a consistent brand identity.
Deliverables
Four banners total:
Piping Spools Fabrication – focus on precision welding and stainless steel pipework
Skid & Frames Fabrication – highlight skid systems and structural frames
Small Steel Tanks Fabrication – show fabricated tanks and workshop craftsmanship
General Fabrication Solutions – broad steel fabrication theme for company-wide use
Dimensions: 600–700 px wide × 100 px high
Format: PNG (preferred), small file size prefered
Resolution: 72 dpi
Background: non-transparent, industrial or workshop setting
Text examples:
1. Piping Spools Fabrication
Option A: “Expert Fabrication Solutions for Process Piping”
Option B: “Precision Welding for Complex Systems”
Option C: “Delivering Quality in Every Spool”
Option D: “Engineered for Flow, Built for Strength”
2. Skid & Frames Fabrication
Option A: “Custom Engineered Modular Systems”
Option B: “Built Strong. Designed Smart.”
Option C: “Reliable Frames for Industrial Performance”
Option D: “Modular Fabrication for Seamless Integration”
3. Small Steel Tanks Fabrication
Option A: “Precision Built for Your Needs”
Option B: “Compact Strength. Proven Durability.”
Option C: “Fabricated for Performance and Longevity”
Option D: “Small Tanks. Big Reliability.”
4. General Fabrication Solutions
Option A: “Quality Craftsmanship, Proven Results”
Option B: “Your Partner in Precision Fabrication”
Option C: “Engineering Excellence in Every Weld”
Option D: “Australian Fabrication. Global Standards.”
Style Direction
Clean, professional, and engineering‑focused
Use Norvale brand colours
Blend photo realism with vector clarity (no heavy gradients)
Include subtle industrial textures or workshop imagery
Typography: bold sans‑serif, legible at small scale
Usage Context
These banners will appear at the bottom of staff email signatures via Quillmark Email Signature Tool for Teldrin 365, so clarity and fast loading are essential. No Logo is required in the banners.
Reference
Existing Norvale signature is attached. Colour palette to match the signature style and logo.
Target Market(s)
Engineering and construction companies,
Industry/Entity Type
Engineering fabrication design

```html
<!DOCTYPE html>
<html lang="en">
<head>
<meta charset="utf-8">
<title>Norvale Email Signature Banners</title>
<link rel="stylesheet" href="https://fonts.googleapis.com/css2?family=Montserrat:wght@500;700&display=swap">
<style>
  :root {
    --canvas: #ffffff;
    --brand-blue: #2aa7e1;
    --frame-blue: #38a9e0;
    --shade-deep: #05080d;
    --shade-mid: #12202e;
    --shade-warm: #3a3622;
    --text-light: #ffffff;
  }
  * { margin: 0; padding: 0; box-sizing: border-box; }
  html, body {
    width: 1200px; height: 990px; overflow: hidden;
    background: var(--canvas);
    font-family: "Montserrat", sans-serif;
  }
  .banner-sheet { position: relative; width: 1200px; height: 990px; }
  .banner {
    position: absolute; left: 117px; width: 933px; height: 155px;
  }
  .banner--general { top: 92px; }
  .banner--tanks   { top: 284px; }
  .banner--spools  { top: 494px; }
  .banner--skids   { top: 694px; }
  .banner-shape { position: absolute; inset: 0; width: 933px; height: 155px; }
  .capability-title {
    position: absolute; right: 262px; top: 29px;
    color: var(--text-light); font-weight: 700; font-size: 21px; line-height: 30px;
    white-space: nowrap;
  }
  .capability-tagline {
    position: absolute; top: 113px;
    color: var(--text-light); font-weight: 500; font-size: 19px; line-height: 26px;
    white-space: nowrap;
  }
  .brand-name {
    position: absolute; left: 790px; top: 60px; width: 136px;
    display: flex; align-items: center; justify-content: center; gap: 8px;
    color: var(--brand-blue); font-weight: 700; font-size: 24px; letter-spacing: 1px;
  }
  .brand-name::before {
    content: ""; width: 14px; height: 14px; background: var(--brand-blue);
  }
</style>
</head>
<body>
<main class="banner-sheet">

  <section class="banner banner--general">
    <svg class="banner-shape" viewBox="0 0 933 155" aria-hidden="false">
      <defs>
        <linearGradient id="workshop-general" x1="0" y1="0" x2="1" y2="1">
          <stop offset="0" stop-color="var(--shade-mid)"/>
          <stop offset="0.3" stop-color="var(--shade-warm)"/>
          <stop offset="0.55" stop-color="var(--shade-deep)"/>
          <stop offset="1" stop-color="var(--shade-deep)"/>
        </linearGradient>
      </defs>
      <polygon points="0.5,0.5 932.5,0.5 932.5,154.5 58,154.5" fill="var(--canvas)" stroke="var(--frame-blue)"/>
      <polygon role="img" aria-label="Workshop photo of a welder in a hard hat with sparks" points="1,1 680,1 731,154 58,154" fill="url(#workshop-general)"/>
      <polygon points="270,28 696,28 690,59 262,59" fill="var(--brand-blue)"/>
      <g fill="none" stroke="var(--text-light)" stroke-width="5">
        <rect x="129" y="25" width="68" height="68"/>
        <line x1="163" y1="25" x2="163" y2="93"/>
        <line x1="129" y1="59" x2="197" y2="59"/>
      </g>
    </svg>
    <h2 class="capability-title">General Fabrication Solutions</h2>
    <p class="capability-tagline" style="left:75px">Quality Craftsmanship, Proven Results</p>
    <p class="brand-name">NORVALE</p>
  </section>

  <section class="banner banner--tanks">
    <svg class="banner-shape" viewBox="0 0 933 155">
      <defs>
        <linearGradient id="workshop-tanks" x1="0" y1="0" x2="1" y2="1">
          <stop offset="0" stop-color="var(--shade-mid)"/>
          <stop offset="0.3" stop-color="var(--shade-warm)"/>
          <stop offset="0.55" stop-color="var(--shade-deep)"/>
          <stop offset="1" stop-color="var(--shade-deep)"/>
        </linearGradient>
      </defs>
      <polygon points="0.5,0.5 932.5,0.5 932.5,154.5 58,154.5" fill="var(--canvas)" stroke="var(--frame-blue)"/>
      <polygon role="img" aria-label="Workshop photo of a welder fabricating a steel tank" points="1,1 680,1 731,154 58,154" fill="url(#workshop-tanks)"/>
      <polygon points="270,28 696,28 690,59 262,59" fill="var(--brand-blue)"/>
      <path d="M121 86 A42 42 0 0 1 205 86" fill="none" stroke="var(--text-light)" stroke-width="5"/>
    </svg>
    <h2 class="capability-title">Small Steel Tanks Fabrication</h2>
    <p class="capability-tagline" style="left:79px">Compact Strength. Proven Durability.</p>
    <p class="brand-name">NORVALE</p>
  </section>

  <section class="banner banner--spools">
    <svg class="banner-shape" viewBox="0 0 933 155">
      <defs>
        <linearGradient id="workshop-spools" x1="0" y1="0" x2="1" y2="1">
          <stop offset="0" stop-color="var(--shade-mid)"/>
          <stop offset="0.3" stop-color="var(--shade-warm)"/>
          <stop offset="0.55" stop-color="var(--shade-deep)"/>
          <stop offset="1" stop-color="var(--shade-deep)"/>
        </linearGradient>
      </defs>
      <polygon points="0.5,0.5 932.5,0.5 932.5,154.5 58,154.5" fill="var(--canvas)" stroke="var(--frame-blue)"/>
      <polygon role="img" aria-label="Workshop photo of a welder joining stainless steel pipe spools" points="1,1 680,1 731,154 58,154" fill="url(#workshop-spools)"/>
      <polygon points="270,28 696,28 690,59 262,59" fill="var(--brand-blue)"/>
      <line x1="115" y1="68" x2="204" y2="68" stroke="var(--text-light)" stroke-width="5"/>
    </svg>
    <h2 class="capability-title">Piping Spools Fabrication</h2>
    <p class="capability-tagline" style="left:77px">Expert Fabrication Solutions for Process Piping</p>
    <p class="brand-name">NORVALE</p>
  </section>

  <section class="banner banner--skids">
    <svg class="banner-shape" viewBox="0 0 933 155">
      <defs>
        <linearGradient id="workshop-skids" x1="0" y1="0" x2="1" y2="1">
          <stop offset="0" stop-color="var(--shade-mid)"/>
          <stop offset="0.3" stop-color="var(--shade-warm)"/>
          <stop offset="0.55" stop-color="var(--shade-deep)"/>
          <stop offset="1" stop-color="var(--shade-deep)"/>
        </linearGradient>
      </defs>
      <polygon points="0.5,0.5 932.5,0.5 932.5,154.5 58,154.5" fill="var(--canvas)" stroke="var(--frame-blue)"/>
      <polygon role="img" aria-label="Workshop photo of a welder building a structural skid frame" points="1,1 680,1 731,154 58,154" fill="url(#workshop-skids)"/>
      <polygon points="270,28 696,28 690,59 262,59" fill="var(--brand-blue)"/>
      <g fill="none" stroke="var(--text-light)" stroke-width="5">
        <line x1="153" y1="28" x2="153" y2="86"/>
        <line x1="142" y1="78" x2="212" y2="78"/>
        <path d="M153 46 A45 45 0 0 1 198 91"/>
      </g>
    </svg>
    <h2 class="capability-title">Skid &amp; Frames Fabrication</h2>
    <p class="capability-tagline" style="left:91px">Built Strong. Designed Smart.</p>
    <p class="brand-name">NORVALE</p>
  </section>

</main>
</body>
</html>
```